Korvane Pty Ltd professional business card

A professional business card template using the colours from the supplied logo.
Clean crisp lines while, Modern while not being over the top.

Target Market(s)

Construction, commerical and industrial

Industry/Entity Type

Communications

Contact Information for Business Card

For a Communications, IT, Optical fibre installation company

Colors
37b8a4

```html
<!DOCTYPE html>
<html lang="en">
<head>
<meta charset="utf-8">
<title>Korvane Pty Ltd – Business Card</title>
<link href="https://fonts.googleapis.com/css2?family=Open+Sans:ital,wght@0,400;0,600;0,700;1,400;1,700&display=swap" rel="stylesheet">
<style>
  :root {
    --teal: #1592a0;
    --grey: #6d6e70;
    --text-grey: #555759;
    --paper: #ffffff;
    --backdrop: #2b2b2d;
  }
  * { margin: 0; padding: 0; box-sizing: border-box; }
  html, body { width: 1200px; height: 900px; overflow: hidden; }
  body {
    background: var(--backdrop);
    font-family: "Open Sans", Arial, sans-serif;
    position: relative;
  }
  .card {
    position: absolute;
    left: 260px;
    width: 680px;
    height: 388px;
    overflow: hidden;
  }
  .card-front { top: 40px; background: var(--paper); }
  .card-back {
    top: 472px;
    background: var(--teal);
    display: flex;
    align-items: center;
    justify-content: center;
  }
  .person { position: absolute; left: 46px; top: 44px; }
  .person-name {
    color: var(--teal);
    font-weight: 700;
    font-style: italic;
    font-size: 25px;
    letter-spacing: 0.5px;
    text-transform: uppercase;
    line-height: 1.1;
  }
  .person-title {
    color: var(--text-grey);
    font-style: italic;
    font-size: 19px;
    margin-top: -2px;
  }
  .divider {
    position: absolute;
    left: 46px;
    top: 124px;
    width: 560px;
    height: 1.5px;
    background: var(--teal);
  }
  .contact-list {
    position: absolute;
    left: 46px;
    top: 140px;
    list-style: none;
    color: var(--text-grey);
    font-size: 18px;
    line-height: 29px;
  }
  .contact-list li { display: flex; align-items: center; gap: 8px; }
  .contact-list svg { width: 15px; height: 15px; fill: var(--teal); }
  .brand {
    position: absolute;
    right: 60px;
    top: 64px;
    display: flex;
    align-items: center;
    gap: 12px;
  }
  .brand-mark { width: 18px; height: 18px; border-radius: 50%; background: var(--teal); }
  .brand-name {
    font-weight: 600;
    font-size: 46px;
    letter-spacing: 3px;
    color: var(--grey);
  }
  .address {
    position: absolute;
    right: 78px;
    top: 210px;
    text-align: right;
    color: var(--text-grey);
    font-style: italic;
    font-size: 19px;
    line-height: 27px;
  }
  .footer-band { position: absolute; left: 0; bottom: 0; width: 680px; height: 120px; }
  .website {
    position: absolute;
    right: 96px;
    bottom: 10px;
    color: var(--paper);
    font-style: italic;
    font-size: 18px;
  }
  .back-brand {
    display: flex;
    align-items: center;
    gap: 18px;
  }
  .back-brand .brand-mark { width: 26px; height: 26px; background: var(--paper); }
  .back-brand .brand-name { color: var(--paper); font-size: 80px; letter-spacing: 5px; }
</style>
</head>
<body>
  <section class="card card-front">
    <div class="person">
      <p class="person-name">Daniel Reyes</p>
      <p class="person-title">President</p>
    </div>
    <div class="divider"></div>
    <ul class="contact-list">
      <li>
        <svg viewBox="0 0 24 24" aria-hidden="true"><path d="M6.6 10.8a15.1 15.1 0 0 0 6.6 6.6l2.2-2.2a1 1 0 0 1 1-.25 11.4 11.4 0 0 0 3.6.57 1 1 0 0 1 1 1V20a1 1 0 0 1-1 1A17 17 0 0 1 3 4a1 1 0 0 1 1-1h3.5a1 1 0 0 1 1 1c0 1.25.2 2.45.57 3.57a1 1 0 0 1-.25 1z"/></svg>
        555-014-2278
      </li>
      <li>
        <svg viewBox="0 0 24 24" aria-hidden="true"><path d="M2 5h20v14H2z M3 6l9 7 9-7" fill="var(--teal)"/><path d="M3 6l9 7 9-7" fill="none" stroke="#fff" stroke-width="1.6"/></svg>
        dreyes@korvane.com
      </li>
    </ul>
    <div class="brand">
      <span class="brand-mark"></span>
      <span class="brand-name">KORVANE</span>
    </div>
    <p class="address">418 Marlow Quay<br>Seacliff CA 92011</p>
    <svg class="footer-band" viewBox="0 0 680 120" preserveAspectRatio="none" aria-hidden="true">
      <path d="M0 28 L310 92 Q330 96 345 92 L360 92 L680 92 L680 120 L0 120 Z" fill="var(--teal)"/>
      <path d="M0 8 L330 86 L310 88 L0 20 Z" fill="var(--grey)"/>
    </svg>
    <p class="website">www.korvanegroup.com</p>
  </section>

  <section class="card card-back">
    <div class="back-brand">
      <span class="brand-mark"></span>
      <span class="brand-name">KORVANE</span>
    </div>
  </section>
</body>
</html>
```